My Billboard for Law Firm

Designing a billboard

Should have
Corvell & Pine, LLC
Ph: 555-214-7390
Auto Accidents / Personal Injury
Family Law
Criminal Defense
Real Estate
Free Consultation

Target Market(s)

Legal

Industry/Entity Type

Legal

Font styles to use
Serif
Sans Serif

Requirements
Must have
• Designing a billboard

Should have
Corvell & Pine, LLC
Ph: 555-214-7390
Family Law
Criminal Defense
Real Estate
Free Consultation
Nice to have
• Nice to have info above
Should not have
• None

```html
<!DOCTYPE html>
<html lang="en">
<head>
<meta charset="utf-8">
<title>Corvell &amp; Pine, LLC — Billboard</title>
<link href="https://fonts.googleapis.com/css2?family=Oranienbaum&family=Poppins:wght@600;700&display=swap" rel="stylesheet">
<style>
  :root {
    --page: #ecebea;
    --brown-deep: #3a2218;
    --brown-mid: #6e5a4f;
    --brown-soft: #a8968b;
    --cream: #ffffff;
    --text-dark: #2f1a12;
    --band: #3b2419;
    --gavel-dark: #3d1f1e;
  }
  html, body {
    margin: 0;
    width: 1200px;
    height: 1181px;
    overflow: hidden;
    background: var(--page);
  }
  .canvas {
    position: relative;
    width: 1200px;
    height: 1181px;
    display: flex;
    align-items: center;
    justify-content: center;
  }
  .billboard {
    position: relative;
    width: 1160px;
    height: 366px;
    overflow: hidden;
    background:
      linear-gradient(180deg, rgba(58,34,24,0.35) 0%, rgba(58,34,24,0) 22%, rgba(58,34,24,0) 80%, rgba(58,34,24,0.25) 100%),
      linear-gradient(90deg, var(--brown-mid) 0%, #c8bab1 12%, var(--cream) 28%, #f4f0ed 46%, var(--brown-soft) 72%, var(--brown-mid) 100%);
  }
  .firm-name {
    position: absolute;
    left: 78px;
    top: 46px;
    margin: 0;
    font-family: "Oranienbaum", serif;
    font-weight: 400;
    font-size: 102px;
    line-height: 96px;
    color: var(--text-dark);
    letter-spacing: 0;
    white-space: nowrap;
  }
  .services {
    position: absolute;
    left: 560px;
    top: 60px;
    margin: 0;
    padding: 0;
    list-style: none;
    font-family: "Poppins", sans-serif;
    font-weight: 700;
    font-size: 21px;
    line-height: 23px;
    letter-spacing: 1.2px;
    color: var(--text-dark);
  }
  .services li {
    position: relative;
    padding-left: 20px;
    margin-bottom: 8px;
  }
  .services li::before {
    content: "";
    position: absolute;
    left: 0;
    top: 8px;
    width: 9px;
    height: 9px;
    border-radius: 50%;
    background: var(--text-dark);
  }
  .phone-band {
    position: absolute;
    left: 0;
    top: 273px;
    width: 840px;
    height: 58px;
    background: var(--band);
  }
  .phone {
    position: absolute;
    left: 80px;
    top: 262px;
    margin: 0;
    font-family: "Poppins", sans-serif;
    font-weight: 700;
    font-size: 55px;
    line-height: 80px;
    letter-spacing: 10px;
    color: var(--cream);
    white-space: nowrap;
  }
  .gavel-photo {
    position: absolute;
    left: 840px;
    top: 40px;
    width: 320px;
    height: 326px;
  }
</style>
</head>
<body>
<main class="canvas">
  <section class="billboard">
    <h1 class="firm-name">CORVELL &amp;<br>PINE LLC</h1>
    <ul class="services">
      <li>AUTO ACCIDENTS /<br>PERSONAL INJURY</li>
      <li>FAMILY LAW</li>
      <li>CRIMINAL DEFENSE</li>
      <li>REAL ESTATE</li>
      <li>FREE CONSULTATION</li>
    </ul>
    <div class="phone-band"></div>
    <p class="phone">PH: 555-214-7390</p>
    <svg class="gavel-photo" viewBox="0 0 320 326" role="img" aria-label="Photo of a wooden judge's gavel with a gold band resting on a round sound block">
      <defs>
        <radialGradient id="gavel-tone" cx="50%" cy="58%" r="48%">
          <stop offset="0%" stop-color="#6b3a36"/>
          <stop offset="60%" stop-color="#3d1f1e"/>
          <stop offset="100%" stop-color="#3d1f1e" stop-opacity="0"/>
        </radialGradient>
      </defs>
      <rect width="320" height="326" fill="url(#gavel-tone)"/>
    </svg>
  </section>
</main>
</body>
</html>
```